Pelling Home Efficiency

Id like for my business card to be very bold and professional. Incorporating the business logo, the main services offered, and my contact info. Services are spray foam, insulation, new construction, retrofit, weatherization.

When opening this project art huddle was not able to upload my new logo that I picked from another recent art huddle project. Does anyone know how i could upload my logo onto the page for design of the business cards?

Target Market(s)

Building owners, contractors

Industry/Entity Type

Building Insulation and performance improvements

Contact Information for Business Card

Owner, Email marcus@pellinghomeefficiency.com Phone number 555-204-6817

Colors
0054AA
0677BA
7BADD7
CADEEF
E8F1F8
F0912C
F2A743
F7CA91
FBE8D2
FDF5EE

Requirements
Must have
• Services- spray foam, cellulose, mineral wool, fiberglass, air sealing, new construction, retrofit, weatherization, energy saving assesments

```html
<!DOCTYPE html>
<html lang="en">
<head>
<meta charset="utf-8">
<title>Pelling Home Efficiency – Business Card</title>
<link href="https://fonts.googleapis.com/css2?family=Poppins:wght@400;500;600;800&display=swap" rel="stylesheet">
<style>
  :root{
    --stage:#2b2c2f;
    --navy:#0c1535;
    --navy-soft:#14244a;
    --navy-warm:#1f1d38;
    --sky:#29abe2;
    --orange:#f0912c;
    --white:#ffffff;
    --muted:#3a4670;
  }
  *{box-sizing:border-box;margin:0;padding:0}
  html,body{width:1200px;height:952px;overflow:hidden;background:var(--stage);font-family:"Poppins",sans-serif}
  .stage{position:relative;width:1200px;height:952px}
  .card{position:absolute;left:240px;width:720px;height:411px;background:var(--navy);border-radius:4px;box-shadow:0 14px 30px rgba(0,0,0,.55);overflow:hidden}
  .card--contact{top:40px}
  .card--services{top:501px}

  .watermark{position:absolute;right:0;bottom:0;width:380px;height:250px;border-top-left-radius:8px;
    background:linear-gradient(135deg,var(--navy-soft) 0%,var(--navy-warm) 100%);opacity:.85}

  .brand{position:absolute;display:flex;align-items:center;gap:12px}
  .brand__mark{width:26px;height:26px;background:var(--sky)}
  .brand__name{color:var(--orange);font-weight:800;font-size:30px;line-height:1.05;letter-spacing:.5px;text-transform:uppercase}
  .card--contact .brand{left:250px;top:60px}
  .card--services .brand{left:320px;top:60px}

  .person{position:absolute;left:80px;top:190px;z-index:1}
  .person__name{color:var(--sky);font-size:30px;font-weight:500;letter-spacing:1px;text-transform:uppercase}
  .person__name strong{font-weight:800}
  .person__role{color:var(--white);font-size:17px;margin-top:2px}
  .person__rule{width:48px;height:2px;background:var(--muted);margin:10px 0 14px}
  .contact{list-style:none}
  .contact li{display:flex;align-items:center;gap:12px;color:var(--white);font-size:16px;margin-bottom:10px}
  .contact__icon{width:26px;height:26px;background:var(--orange);border-radius:3px;display:flex;align-items:center;justify-content:center}

  .services{position:absolute;left:48px;right:40px;top:190px;display:grid;grid-template-columns:repeat(3,auto);column-gap:30px;justify-content:start}
  .services ul{list-style:none}
  .services li{display:flex;align-items:center;gap:8px;color:var(--white);font-size:14px;font-weight:500;margin-bottom:10px;white-space:nowrap}
  .tick{flex:none}
</style>
</head>
<body>
<main class="stage">

  <section class="card card--contact" aria-label="Business card front">
    <div class="watermark" role="img" aria-label="Large faint brand watermark in deep navy tones"></div>
    <div class="brand">
      <span class="brand__mark"></span>
      <span class="brand__name">Pelling Home<br>Efficiency</span>
    </div>
    <div class="person">
      <h1 class="person__name">Daniel R. <strong>Wexford</strong></h1>
      <p class="person__role">Owner</p>
      <div class="person__rule"></div>
      <ul class="contact">
        <li><span class="contact__icon">
          <svg width="16" height="16" viewBox="0 0 24 24"><path fill="#fff" d="M6.6 10.8a15 15 0 0 0 6.6 6.6l2.2-2.2a1 1 0 0 1 1-.25 11.4 11.4 0 0 0 3.6.57 1 1 0 0 1 1 1V20a1 1 0 0 1-1 1A17 17 0 0 1 3 4a1 1 0 0 1 1-1h3.5a1 1 0 0 1 1 1c0 1.25.2 2.45.57 3.57a1 1 0 0 1-.25 1z"/></svg>
        </span>+555-204-6817</li>
        <li><span class="contact__icon">
          <svg width="16" height="16" viewBox="0 0 24 24"><path fill="none" stroke="#fff" stroke-width="2" d="M3 6h18v12H3zM3 6l9 7 9-7"/></svg>
        </span>marcus@pellinghomeefficiency.com</li>
      </ul>
    </div>
  </section>

  <section class="card card--services" aria-label="Business card back">
    <div class="brand">
      <span class="brand__mark"></span>
      <span class="brand__name">Pelling Home<br>Efficiency</span>
    </div>
    <div class="services">
      <ul>
        <li><svg class="tick" width="16" height="16" viewBox="0 0 16 16"><rect x="1" y="3" width="12" height="12" fill="none" stroke="#29abe2" stroke-width="1.6"/><path d="M4 9l3 3 7-9" fill="none" stroke="#f0912c" stroke-width="2"/></svg>Services- Spray Foam</li>
        <li><svg class="tick" width="16" height="16" viewBox="0 0 16 16"><rect x="1" y="3" width="12" height="12" fill="none" stroke="#29abe2" stroke-width="1.6"/><path d="M4 9l3 3 7-9" fill="none" stroke="#f0912c" stroke-width="2"/></svg>Cellulose</li>
        <li><svg class="tick" width="16" height="16" viewBox="0 0 16 16"><rect x="1" y="3" width="12" height="12" fill="none" stroke="#29abe2" stroke-width="1.6"/><path d="M4 9l3 3 7-9" fill="none" stroke="#f0912c" stroke-width="2"/></svg>Mineral Wool</li>
      </ul>
      <ul>
        <li><svg class="tick" width="16" height="16" viewBox="0 0 16 16"><rect x="1" y="3" width="12" height="12" fill="none" stroke="#29abe2" stroke-width="1.6"/><path d="M4 9l3 3 7-9" fill="none" stroke="#f0912c" stroke-width="2"/></svg>Fiberglass</li>
        <li><svg class="tick" width="16" height="16" viewBox="0 0 16 16"><rect x="1" y="3" width="12" height="12" fill="none" stroke="#29abe2" stroke-width="1.6"/><path d="M4 9l3 3 7-9" fill="none" stroke="#f0912c" stroke-width="2"/></svg>Air Sealing</li>
        <li><svg class="tick" width="16" height="16" viewBox="0 0 16 16"><rect x="1" y="3" width="12" height="12" fill="none" stroke="#29abe2" stroke-width="1.6"/><path d="M4 9l3 3 7-9" fill="none" stroke="#f0912c" stroke-width="2"/></svg>New Construction</li>
      </ul>
      <ul>
        <li><svg class="tick" width="16" height="16" viewBox="0 0 16 16"><rect x="1" y="3" width="12" height="12" fill="none" stroke="#29abe2" stroke-width="1.6"/><path d="M4 9l3 3 7-9" fill="none" stroke="#f0912c" stroke-width="2"/></svg>Retrofit</li>
        <li><svg class="tick" width="16" height="16" viewBox="0 0 16 16"><rect x="1" y="3" width="12" height="12" fill="none" stroke="#29abe2" stroke-width="1.6"/><path d="M4 9l3 3 7-9" fill="none" stroke="#f0912c" stroke-width="2"/></svg>Weatherization</li>
        <li><svg class="tick" width="16" height="16" viewBox="0 0 16 16"><rect x="1" y="3" width="12" height="12" fill="none" stroke="#29abe2" stroke-width="1.6"/><path d="M4 9l3 3 7-9" fill="none" stroke="#f0912c" stroke-width="2"/></svg>Energy Saving Assesments</li>
      </ul>
    </div>
  </section>

</main>
</body>
</html>
```